Holistic/ Sports Psychologist needs flyer design

I need a flyer designed that catches the attention of potential customers - (parents of young athletes and athletes) who may be looking for psychological services. I have a logo and all the relevant info for the flyer but would like someone to take it and make it look creative, fun, fresh and attention getting for high school and college athletes. The colors used can be from my logo design which represents my holistic approach.
Target Market(s)
high school and collegiate athletes
Industry/Entity Type
sports psychology
Requirements
Must have
- Info I put on the flyer with my logo and please add some graphics and color based on my logo

```html
<!DOCTYPE html>
<html lang="en">
<head>
<meta charset="utf-8">
<title>Holistic and Sports Psychology Consulting – Flyer</title>
<link rel="stylesheet" href="https://fonts.googleapis.com/css2?family=Great+Vibes&family=Poppins:ital,wght@0,300;0,400;0,500;0,600;0,700;1,400&family=Oswald:wght@500&family=Montserrat:wght@800&display=swap">
<style>
  :root{
    --mat:#8c8c8c;
    --purple:#6657a6;
    --purple-dark:#4a3f86;
    --green:#a8d174;
    --green-soft:#d8ebbd;
    --ink:#1d1b3a;
    --text:#2d2d2d;
    --white:#ffffff;
    --sky:#dce9f0;
  }
  *{box-sizing:border-box;margin:0;padding:0}
  html,body{width:917px;height:1200px;overflow:hidden;background:var(--mat)}
  body{position:relative;font-family:"Poppins",sans-serif;color:var(--text)}

  .flyer{position:absolute;left:130px;top:106px;width:657px;height:986px;background:var(--white);overflow:hidden}
  .flyer > *{position:absolute}

  .backdrop{left:0;top:0;width:657px;height:986px}

  .brand{left:29px;top:26px;display:flex;align-items:center;gap:5px}
  .brand-mark{width:32px;height:32px;border-radius:50%;background:var(--sky);border:2px solid var(--purple)}
  .brand-name{font-size:8.5px;color:var(--purple);border-bottom:5px solid var(--green);padding:0 0 1px 2px;width:110px}

  .title{left:26px;top:70px;font-family:"Great Vibes",cursive;font-weight:400;font-size:34px;line-height:46px;color:var(--ink);white-space:nowrap}

  .hero-photo{left:362px;top:9px;width:282px;height:282px;border-radius:50%;border:9px solid var(--white);
    background:radial-gradient(circle at 50% 30%,#fde7a4 0%,#f2b457 22%,#8c6a3a 48%,#3f3a2a 70%,#7d7568 100%)}

  .headline{left:25px;top:282px;line-height:1;font-weight:400}
  .headline-lead{font-size:37px;font-weight:300;color:#2b2b2b;display:block}
  .headline-main{font-size:26px;font-weight:700;color:var(--purple);display:block;margin-top:4px}
  .headline-sub{font-size:18px;font-weight:400;color:#2b2b2b;display:block;margin-top:4px}

  .service{width:254px}
  .service-bar{position:relative;height:38px;border-radius:0 0 12px 0;display:flex;align-items:center;padding-left:48px;font-size:14px;font-weight:600;white-space:nowrap}
  .service-bar.is-purple{background:var(--purple);color:var(--white)}
  .service-bar.is-green{background:var(--green);color:var(--purple-dark)}
  .service-icon{position:absolute;left:0;top:-2px;width:42px;height:42px;border-radius:50%;background:var(--white);border:2px solid #e3e0f0;display:flex;align-items:center;justify-content:center}
  .service-icon span{width:22px;height:22px;border-radius:50%;background:linear-gradient(135deg,var(--green),var(--purple));opacity:.75}
  .service-text{margin:12px 0 0 9px;font-size:11px;line-height:14px;color:var(--ink);font-weight:500}

  .svc-skills{left:27px;top:388px}
  .svc-health{left:27px;top:501px}
  .svc-injury{left:28px;top:614px}
  .svc-injury .service-text{width:270px}
  .svc-perf{left:345px;top:386px}
  .svc-perf .service-bar{padding-left:46px}
  .svc-burnout{left:345px;top:501px}
  .svc-burnout .service-text{width:260px}

  .action-art{left:300px;top:630px;width:332px;height:126px;border-radius:8px;
    background:linear-gradient(100deg,rgba(255,255,255,0) 0%,#c9c3e2 35%,#6a5fa8 62%,#b86a3f 82%,#e88c3a 100%);opacity:.85}

  .divider{left:27px;top:758px;width:576px;height:1px;background:var(--purple)}

  .bio{left:29px;top:771px;width:576px;font-size:9.1px;line-height:13.6px;font-style:italic;color:#333}
  .bio p + p{margin-top:13.6px;text-align:justify}

  .session-box{left:331px;top:858px;width:272px;height:57px;border:1px solid rgba(255,255,255,.9);text-align:right;padding:8px 7px 0 0;white-space:nowrap}
  .session-note{font-size:10.5px;font-weight:600;color:var(--ink);line-height:14px}
  .session-length{font-family:"Oswald",sans-serif;font-weight:500;font-size:22px;line-height:28px;color:var(--purple);letter-spacing:-.6px}

  .contact-label{left:28px;top:911px;font-size:11px;font-weight:600;color:var(--white)}
  .contact{top:946px;display:flex;align-items:center;gap:7px;color:var(--white);white-space:nowrap}
  .contact-icon{width:17px;height:17px;border-radius:50%;background:var(--green);display:flex;align-items:center;justify-content:center;flex:none}
  .contact-address{left:27px;font-size:10.5px;line-height:14px}
  .contact-web{left:217px;top:952px;font-size:11px;font-weight:500;letter-spacing:.6px}
  .contact-phone{left:423px;top:950px;font-family:"Montserrat",sans-serif;font-weight:800;font-size:19px;letter-spacing:.5px}
</style>
</head>
<body>
<main class="flyer">
  <svg class="backdrop" viewBox="0 0 657 986" aria-hidden="true">
    <defs>
      <linearGradient id="sky-wash" x1="0" y1="0" x2="1" y2="1">
        <stop offset="0" stop-color="#efe3dd"/>
        <stop offset=".45" stop-color="#f7d9bf"/>
        <stop offset=".7" stop-color="#eef0ee"/>
        <stop offset="1" stop-color="#d6e7ef"/>
      </linearGradient>
      <linearGradient id="meadow" x1="0" y1="0" x2="1" y2="0">
        <stop offset="0" stop-color="#ffffff" stop-opacity="0"/>
        <stop offset=".35" stop-color="#e4f1d3"/>
        <stop offset="1" stop-color="#a8d174"/>
      </linearGradient>
    </defs>
    <rect width="657" height="400" fill="url(#sky-wash)"/>
    <path d="M0,262 C60,220 110,205 160,205 C260,205 380,290 470,296 C560,300 620,285 657,267 L657,420 L0,420Z" fill="#6657a6"/>
    <path d="M0,292 C60,242 110,220 170,220 C280,222 400,320 490,330 C580,338 630,325 657,317 L657,420 L0,420Z" fill="#a8d174"/>
    <path d="M0,300 C60,252 110,232 170,232 C300,232 420,345 530,368 C600,380 640,360 657,348 L657,986 L0,986Z" fill="#ffffff"/>
    <path d="M260,905 C350,840 540,822 657,818 L657,895 C630,905 590,925 520,930 C420,935 330,888 260,905Z" fill="url(#meadow)"/>
    <path d="M0,908 C80,870 150,862 230,872 C330,885 420,935 520,930 C590,925 630,905 657,895 L657,986 L0,986Z" fill="#6657a6"/>
  </svg>

  <div class="brand">
    <span class="brand-mark"></span>
    <span class="brand-name">Dr. Elena Hartwell</span>
  </div>

  <h1 class="title">Holistic Psychology and<br>Sports Psychology<br>Consulting</h1>

  <div class="hero-photo" role="img" aria-label="Photo of a woman with raised joined hands in a yoga pose against a sunset over a lake"></div>

  <h2 class="headline">
    <span class="headline-lead">Ways to Improve</span>
    <span class="headline-main">ATHLETIC PERFORMANCE</span>
    <span class="headline-sub">Using Sports and Holistic Psychology</span>
  </h2>

  <section class="service svc-skills">
    <div class="service-bar is-purple"><span class="service-icon"><span></span></span>Mental Skills Training</div>
    <p class="service-text">Ex: visualization, goal-setting,motivation, self- talk, mindset, concentration techniques</p>
  </section>

  <section class="service svc-health">
    <div class="service-bar is-green"><span class="service-icon"><span></span></span>Mental Health</div>
    <p class="service-text">Anxiety and stress management by using relaxation techniques, breathwork, and mindfulness practices</p>
  </section>

  <section class="service svc-injury">
    <div class="service-bar is-purple"><span class="service-icon"><span></span></span>Injury Recovery Support</div>
    <p class="service-text">Assist athletes in maintaining resilience and positive mental attitude during rehabilitation as well as processing emotions relating to any potential trauma caused by the injury or life transitions resulting from it.</p>
  </section>

  <section class="service svc-perf">
    <div class="service-bar is-green"><span class="service-icon"><span></span></span>Performance Enhancement</div>
    <p class="service-text">Eliminate psychological barriers that are hindering performance such as self- doubt, perfectionism, fear of failure, and burnout</p>
  </section>

  <section class="service svc-burnout">
    <div class="service-bar is-purple"><span class="service-icon"><span></span></span>Burnout prevention</div>
    <p class="service-text">Teach athletes how to have balance in sports and life so they can experience longevity in their sports as well as overall optimal health and well-being.</p>
  </section>

  <div class="action-art" role="img" aria-label="Illustration of a sprinting athlete made of particles, next to a group of sports balls"></div>

  <div class="divider"></div>

  <div class="bio">
    <p>Dr. Elena Hartwell is a licensed psychologist. She understands the unique experiences of athletes due to her background as an All-American swimmer, collegiate and age group swim coach, parent of a collegiate/professional athlete, and sports psychology researcher. She works with athletes to optimize performance and overall well-being.</p>
    <p>Her specializations include: performance anxiety, mental performance, stress management, anxiety, depressions, trauma, life transitions, relationship issues, injury, and sleep</p>
  </div>

  <div class="session-box">
    <p class="session-note">All services are provided online via telehealth.</p>
    <p class="session-length">Sessions are 30 or 55 minutes.</p>
  </div>

  <p class="contact-label">Contact info:</p>

  <div class="contact contact-address">
    <span class="contact-icon"><svg width="9" height="11" viewBox="0 0 9 11"><path d="M4.5 0.5a3.5 3.5 0 0 1 3.5 3.5c0 2.6-3.5 6.5-3.5 6.5S1 6.6 1 4a3.5 3.5 0 0 1 3.5-3.5z" fill="#6657a6"/><circle cx="4.5" cy="4" r="1.3" fill="#a8d174"/></svg></span>
    <span>2280 Harbor Lane #105<br>Seaside Point, FL 32000</span>
  </div>

  <div class="contact contact-web">
    <span class="contact-icon"><svg width="11" height="11" viewBox="0 0 11 11" fill="none" stroke="#6657a6" stroke-width="1"><circle cx="5.5" cy="5.5" r="4.5"/><ellipse cx="5.5" cy="5.5" rx="2" ry="4.5"/><path d="M1 5.5h9"/></svg></span>
    <span>www.drelenahartwell.com</span>
  </div>

  <div class="contact contact-phone">
    <span class="contact-icon"><svg width="10" height="10" viewBox="0 0 10 10"><path d="M2 0.8l1.6 0.2 0.7 2-1 1c0.6 1.2 1.5 2.1 2.7 2.7l1-1 2 0.7 0.2 1.6c-0.3 0.8-1 1.2-1.8 1.2C4 9 1 6 0.8 2.6 0.8 1.8 1.2 1.1 2 0.8z" fill="#6657a6"/></svg></span>
    <span>555-014-2390</span>
  </div>
</main>
</body>
</html>
```